Web Site - Holloway-Strength.com

Design a 3 page web site for Holloway Strength. See attached design brief.
Holloway Strength - Web Site
www.holloway-strength.com

Design a 3 page web site for Holloway Strength, a small local fitness center that provided cardio and weights only (machines and free weights). There are no classes or other services offered at this facility. Holloway Strength is an affordable alternative to the big box, expensive fitness centers. It is small, local, convenient and a community oriented place to work out.
web site can be clean, simple and communicate basic information about the company and membership offers. Although the branding is black, orange and gray, the web site colors should be soft, light and neutral colors that will appeal to both men and women.
Text: Input generic text during design for each text area that will be modified later during the coding phase. The selected designer is expected to code the site and deliver all compressive files (images, files and code) for an unrestricted hand off and full ownership of all content by the client for future modifications by others.

Images
Images used can be generic royalty free images of people working out, on cardio machines, lifting on universal equipment, stretching or lifting weights or images with out people i.e a yoga mat, free weights, a row of cardio machines etc. This is an adults only facility - images can be a mix of men and women and of diverse multi ethnic backgrounds. Image of the actual gym are included below but should NOT be used on the web site.

Branding - See attached for vertical and horizontal logos for Holloway Strength. These can be used in any way and should be incorporated into the web site
WEB SITE OUTLINE
THREE web pages - Pages can be individual pages clicked through to each page from a navigation area but ALSO pages can be “blend together” into one long scrolling “home” or primary landing page.
1) Home Page with basic information
2) Membership Page (to be later integrated with Quillmark member software to show changing membership specials). - see example below - all text will change later
3) contact page - address - telephone number - google map directions
www.holloway-strength.com
Address:
Located in Tannery Brook Commons
418 E. Walnut Lane, Suite 305, Limerick PA 19468
Tel: 484-555-0172

Target Market(s)

Men and Women - Adults over 18,

Industry/Entity Type

Fitness, Work Out, Gym

Coding

Coded - Design and coding required

Number of Pages Required

3 page

Requirements
Must have
• See Project Brief
Should not have
• Dark Colors that feel too masculine

```html
<!DOCTYPE html>
<html lang="en">
<head>
<meta charset="UTF-8">
<title>Holloway Strength – Membership</title>
<link rel="stylesheet" href="https://fonts.googleapis.com/css2?family=DM+Sans:wght@400;500;600&family=Unbounded:wght@700;800&display=swap">
<style>
  :root {
    --orange: #f26a12;
    --ink: #2b2420;
    --soft-ink: #4a403a;
    --card: #f7f3ee;
    --page: #ffffff;
    --hero-top: #d8cfc4;
    --hero-bottom: #e6dfd6;
    --footer-bg: #eee8e0;
    --rule: #bdb4a9;
  }
  * { box-sizing: border-box; margin: 0; padding: 0; }
  html, body { width: 1100px; height: 1200px; overflow: hidden; }
  body {
    position: relative;
    background: var(--page);
    font-family: "DM Sans", sans-serif;
    color: var(--ink);
  }
  .hero-photo {
    position: absolute; left: 0; top: 0; width: 1100px; height: 802px;
    background:
      radial-gradient(ellipse at 30% 35%, #e9e2d9 0%, transparent 55%),
      radial-gradient(ellipse at 75% 30%, #e4dcd2 0%, transparent 50%),
      linear-gradient(180deg, var(--hero-top) 0%, var(--hero-bottom) 100%);
  }
  .brand {
    position: absolute; display: flex; align-items: center; gap: 10px;
    color: var(--ink); font-weight: 600; text-transform: uppercase;
    letter-spacing: 2px; line-height: 1.05;
  }
  .brand-dot { width: 14px; height: 14px; border-radius: 50%; background: var(--orange); flex: none; }
  .site-header .brand { left: 74px; top: 36px; font-size: 17px; }
  .footer-brand { left: 111px; top: 1018px; font-size: 21px; }
  .main-nav a, .footer-nav a {
    position: absolute; color: var(--ink); text-decoration: none; font-size: 11px;
  }
  .nav-cta {
    position: absolute; left: 896px; top: 35px; width: 130px; height: 36px;
    border-radius: 18px; background: var(--orange); color: #ffffff;
    font-size: 11px; display: flex; align-items: center; justify-content: center;
    text-decoration: none;
  }
  .eyebrow {
    position: absolute; left: 0; width: 1100px; top: 180px; text-align: center;
    color: var(--soft-ink); font-size: 13px; letter-spacing: 1.5px;
  }
  .hero-title {
    position: absolute; left: 0; width: 1100px; top: 203px; text-align: center;
    font-family: "Unbounded", sans-serif; font-weight: 800; font-size: 39px;
    line-height: 45px; color: var(--ink); letter-spacing: 0.5px;
  }
  .accent { color: var(--orange); }
  .plan-card {
    position: absolute; top: 344px; width: 409px; height: 582px;
    background: var(--card); border-radius: 12px;
    box-shadow: 0 18px 40px rgba(60,40,20,0.10);
  }
  .plan-card.signature { left: 129px; }
  .plan-card.young { left: 561px; }
  .plan-name {
    position: absolute; top: 43px; width: 100%; text-align: center;
    font-family: "Unbounded", sans-serif; font-weight: 700; font-size: 23px; line-height: 27px;
  }
  .plan-tagline {
    position: absolute; top: 105px; width: 100%; text-align: center; font-size: 13px;
  }
  .plan-rule { position: absolute; left: 23px; right: 23px; height: 1px; background: var(--rule); }
  .plan-rule.top { top: 140px; }
  .plan-rule.bottom { top: 436px; }
  .plan-features { position: absolute; top: 171px; left: 35px; list-style: none; }
  .plan-features li {
    display: flex; align-items: center; gap: 8px; height: 24.4px; font-size: 13.5px;
  }
  .plan-features svg { width: 12px; height: 12px; flex: none; }
  .plan-price {
    position: absolute; top: 460px; width: 100%; text-align: center;
    font-size: 33px; font-weight: 400;
  }
  .plan-price sup { font-size: 17px; vertical-align: 14px; }
  .plan-price .per { font-size: 18px; vertical-align: 14px; }
  .plan-select {
    position: absolute; top: 508px; left: 114px; width: 181px; height: 41px;
    border-radius: 21px; background: var(--orange); color: #ffffff;
    font-size: 13px; font-weight: 500; display: flex; align-items: center; justify-content: center;
    text-decoration: none;
  }
  .site-footer {
    position: absolute; left: 0; top: 984px; width: 1100px; height: 216px; background: var(--footer-bg);
  }
  .copyright {
    position: absolute; left: 111px; top: 1150px; color: var(--soft-ink); font-size: 11px;
  }
</style>
</head>
<body>
  <div class="hero-photo" role="img" aria-label="Softly lit gym interior with people training on cardio machines"></div>

  <header class="site-header">
    <div class="brand"><span class="brand-dot"></span><span>Holloway<br>Strength</span></div>
    <nav class="main-nav">
      <a href="#" style="left:662px;top:47px">Home</a>
      <a href="#" style="left:737px;top:47px">About Us</a>
      <a href="#" style="left:828px;top:47px">Services</a>
    </nav>
    <a class="nav-cta" href="#">Contact Us</a>
  </header>

  <p class="eyebrow">CONTACT US</p>
  <h1 class="hero-title">Your Success <span class="accent">Starts</span><br><span class="accent">With</span> the Right Plan</h1>

  <svg width="0" height="0" style="position:absolute">
    <symbol id="tick" viewBox="0 0 12 12"><path d="M1 6.5 L4.5 10 L11 1.5" fill="none" stroke="#f26a12" stroke-width="2.4" stroke-linecap="round" stroke-linejoin="round"/></symbol>
  </svg>

  <section class="plan-card signature">
    <h2 class="plan-name">Signature<br>Membership</h2>
    <p class="plan-tagline">Donec efficitur justo quis est auctor sodales</p>
    <div class="plan-rule top"></div>
    <ul class="plan-features">
      <li><svg><use href="#tick"/></svg>Sed in aliquam turpis Quisque vel ligula</li>
      <li><svg><use href="#tick"/></svg>Sed turpis consectetur tempus.</li>
      <li><svg><use href="#tick"/></svg>Aenean tristique sem vel sem auctor</li>
      <li><svg><use href="#tick"/></svg>Maximus vel in nulla.</li>
      <li><svg><use href="#tick"/></svg>Praesent facilisis nisi turpis.</li>
      <li><svg><use href="#tick"/></svg>Proin accumsan ligula a augue mattis</li>
      <li><svg><use href="#tick"/></svg>Nec tempus leo pretium.</li>
      <li><svg><use href="#tick"/></svg>Pellentesque ac luctus turpis.</li>
      <li><svg><use href="#tick"/></svg>Duis maximus augue ut massa lacinia</li>
      <li><svg><use href="#tick"/></svg>Nec efficitur arcu porta.</li>
    </ul>
    <div class="plan-rule bottom"></div>
    <p class="plan-price"><sup>$</sup>199<span class="per">/mo</span></p>
    <a class="plan-select" href="#">Select Membership</a>
  </section>

  <section class="plan-card young">
    <h2 class="plan-name">26 &amp; Under<br>Membership</h2>
    <p class="plan-tagline">Donec efficitur justo quis est auctor sodales</p>
    <div class="plan-rule top"></div>
    <ul class="plan-features">
      <li><svg><use href="#tick"/></svg>Sed in aliquam turpis Quisque vel ligula</li>
      <li><svg><use href="#tick"/></svg>Sed turpis consectetur tempus.</li>
      <li><svg><use href="#tick"/></svg>Aenean tristique sem vel sem auctor</li>
      <li><svg><use href="#tick"/></svg>Maximus vel in nulla.</li>
      <li><svg><use href="#tick"/></svg>Praesent facilisis nisi turpis.</li>
      <li><svg><use href="#tick"/></svg>Proin accumsan ligula a augue mattis</li>
      <li><svg><use href="#tick"/></svg>Nec tempus leo pretium.</li>
      <li><svg><use href="#tick"/></svg>Pellentesque ac luctus turpis.</li>
      <li><svg><use href="#tick"/></svg>Duis maximus augue ut massa lacinia</li>
      <li><svg><use href="#tick"/></svg>Nec efficitur arcu porta.</li>
    </ul>
    <div class="plan-rule bottom"></div>
    <p class="plan-price"><sup>$</sup>179<span class="per">/mo</span></p>
    <a class="plan-select" href="#">Select Membership</a>
  </section>

  <footer class="site-footer"></footer>
  <div class="brand footer-brand"><span class="brand-dot"></span><span>Holloway<br>Strength</span></div>
  <nav class="footer-nav">
    <a href="#" style="left:780px;top:1047px">Home</a>
    <a href="#" style="left:854px;top:1047px">About Us</a>
    <a href="#" style="left:945px;top:1047px">Services</a>
  </nav>
  <p class="copyright">© Copyright 2026 | HOLLOWAY STRENGTH | All Right Reserved</p>
</body>
</html>
```